Letterhead/Envelope Design Project

We are a 501c3 non-profit that supports educational programs at Oskenna Ridge Meadows State Park in California. We have new logo and need letterhead. The design needs need incorporate the logo attached. It needs to contain the information in document attached called "information" attached. Please see our website ridgemeadows.org to get the feeling and colors we are looking for.

```html
<!DOCTYPE html>
<html lang="en">
<head>
<meta charset="utf-8">
<title>Oskenna Ridge Meadows Association – Envelope</title>
<link rel="stylesheet" href="https://fonts.googleapis.com/css2?family=Roboto:wght@400;700&family=Roboto+Condensed:wght@700&family=Pinyon+Script&display=swap">
<style>
  :root {
    --forest: #1b5120;
    --ink: #1a5020;
    --paper: #ffffff;
    --edge: #c8c8c8;
  }
  html, body {
    margin: 0;
    width: 1200px;
    height: 1200px;
    overflow: hidden;
    background: var(--paper);
  }
  .canvas {
    position: relative;
    width: 1200px;
    height: 1200px;
  }
  .envelope-shape {
    position: absolute;
    left: 0;
    top: 0;
  }
  .flap-content {
    position: absolute;
    left: 138px;
    top: 200px;
    width: 924px;
    height: 147px;
    display: flex;
    align-items: center;
    justify-content: center;
    gap: 20px;
    transform: rotate(180deg);
    color: var(--paper);
  }
  .tagline {
    position: relative;
    top: 8px;
    font-family: "Pinyon Script", cursive;
    font-size: 30px;
    line-height: 1;
    white-space: nowrap;
  }
  .flap-name {
    position: relative;
    top: 28px;
    width: 80px;
    font-family: "Roboto Condensed", sans-serif;
    font-weight: 700;
    font-size: 11px;
    line-height: 1.05;
    text-transform: uppercase;
    text-align: center;
  }
  .return-block {
    position: absolute;
    left: 181px;
    top: 414px;
    color: var(--ink);
  }
  .org-name {
    width: 148px;
    height: 174px;
    margin: 0;
    display: flex;
    flex-direction: column;
    justify-content: flex-end;
    font-family: "Roboto Condensed", sans-serif;
    font-weight: 700;
    font-size: 22px;
    line-height: 1.08;
    text-transform: uppercase;
  }
  .return-address {
    margin: 24px 0 0;
    font-family: "Roboto", sans-serif;
    font-style: normal;
    font-size: 13px;
    line-height: 18px;
  }
</style>
</head>
<body>
<div class="canvas">
  <svg class="envelope-shape" width="1200" height="1200" viewBox="0 0 1200 1200" aria-hidden="true">
    <rect class="envelope-body" x="110.5" y="347.5" width="979" height="652" fill="var(--paper)" stroke="var(--edge)" stroke-width="1"/>
    <path class="envelope-flap" d="M110 347 L132 235 Q140 200 185 200 L1015 200 Q1060 200 1068 235 L1090 347 Z" fill="var(--forest)"/>
  </svg>

  <div class="flap-content">
    <span class="tagline">Wander in Wonder</span>
    <span class="flap-name">Oskenna Ridge Meadows Association</span>
    <span class="tagline">Beneath the Pines</span>
  </div>

  <div class="return-block">
    <p class="org-name"><span>Oskenna</span><span>Ridge Meadows</span><span>Association</span></p>
    <address class="return-address">P.O. Box 4820<br>Pinecrest Falls, CA&nbsp; 95990-4820</address>
  </div>
</div>
</body>
</html>
```